Marlo's Pizzeria BOGO Promotion Pizza Flyer (Huron)

Pizzeria flyer promoting "under new management" and then the main point for this flyer is our Buy One Get One Free promotion on our pizzas (disclaimer: not valid for Mini Feast Tray or Crowd Pies)(we reserve the right to cancel this promotion at any time)
This promotion has no limit and can be carryout or delivery. No coupon needed.
Looking for a fun bright flyer with our logo colors

Requirements
Must have
• Store Info
• 287 Wexford Rd. E
• Huron, OH
• 419-867-2093
• Open at 4pm Daily!

```html
<!DOCTYPE html>
<html lang="en">
<head>
<meta charset="utf-8">
<title>Marlo's Pizzeria – Buy One Get One Free</title>
<link href="https://fonts.googleapis.com/css2?family=Bebas+Neue&family=Alfa+Slab+One&family=Roboto+Slab:wght@700;800&family=Poppins:wght@600;700&display=swap" rel="stylesheet">
<style>
  :root {
    --stage: #e9e6e2;
    --ink: #1a1512;
    --dark: #2a211c;
    --red: #e1141b;
    --red-deep: #a80d12;
    --white: #ffffff;
    --cream: #fff4e2;
    --crust: #d99a4e;
    --wood: #6b4528;
    --wood-dark: #3a2417;
  }
  * { box-sizing: border-box; margin: 0; padding: 0; }
  html, body { width: 1200px; height: 1200px; overflow: hidden; }
  body { background: var(--stage); position: relative; }

  .flyer {
    position: absolute; left: 195px; top: 45px;
    width: 810px; height: 1110px;
    background: linear-gradient(180deg, var(--dark) 0%, #3b2a22 45%, var(--wood-dark) 100%);
    overflow: hidden;
    box-shadow: 0 14px 40px rgba(0,0,0,.25);
  }

  .photo-hero {
    position: absolute; left: 0; top: 520px; width: 810px; height: 330px;
    background: radial-gradient(ellipse 70% 55% at 55% 55%, #f2c27a 0%, #d9843f 35%, #8a3d1f 70%, rgba(58,36,23,0) 100%);
  }
  .photo-table {
    position: absolute; left: 0; top: 800px; width: 810px; height: 200px;
    background: linear-gradient(180deg, #9c6a40 0%, var(--wood) 45%, var(--wood-dark) 100%);
  }
  .photo-toppings {
    position: absolute; right: -40px; top: -40px; width: 320px; height: 240px;
    border-radius: 50%;
    background: radial-gradient(circle at 60% 55%, #e7a95a 0%, #c2682c 40%, rgba(42,33,28,0) 72%);
  }

  .splash {
    position: absolute; left: 100px; top: 120px; width: 620px; height: 420px;
    border-radius: 48% 52% 40% 60% / 55% 45% 55% 45%;
    background: radial-gradient(ellipse at 50% 45%, var(--red) 0%, var(--red) 55%, var(--red-deep) 80%, rgba(168,13,18,0) 100%);
  }

  .brand {
    position: absolute; left: 60px; top: 75px;
    display: flex; align-items: center; gap: 12px;
  }
  .brand-dot { width: 26px; height: 26px; border-radius: 50%; background: var(--red); }
  .brand-name {
    font-family: "Roboto Slab", serif; font-weight: 800;
    font-size: 30px; color: var(--white);
  }

  .headline { position: absolute; left: 0; right: 0; top: 190px; text-align: center; }
  .headline-top {
    font-family: "Bebas Neue", sans-serif; font-size: 108px; line-height: 1;
    color: var(--white); letter-spacing: 1px;
  }
  .headline-free {
    font-family: "Alfa Slab One", serif; font-size: 190px; line-height: .95;
    color: var(--ink); letter-spacing: 4px;
    text-shadow: 3px 3px 0 var(--white), -2px -2px 0 var(--white), 2px -2px 0 var(--white), -2px 2px 0 var(--white);
  }

  .hours-pill {
    position: absolute; left: 130px; top: 498px; width: 550px; height: 70px;
    border-radius: 14px;
    background: linear-gradient(180deg, #ff3b2c 0%, var(--red) 50%, var(--red-deep) 100%);
    box-shadow: 0 0 0 3px #f6b23b, 0 6px 16px rgba(0,0,0,.4);
    display: flex; align-items: center; justify-content: center;
    font-family: "Roboto Slab", serif; font-weight: 800; font-size: 36px;
    color: var(--white); letter-spacing: 1px;
  }

  .terms {
    position: absolute; left: 40px; right: 40px; top: 880px; text-align: center;
    font-family: "Roboto Slab", serif; font-weight: 700;
  }
  .terms-line { font-size: 24px; color: var(--white); line-height: 1.4; }
  .terms-note { font-size: 19px; color: var(--red); margin-top: 6px; }

  .store-band {
    position: absolute; left: 0; bottom: 0; width: 810px; height: 100px;
    background: linear-gradient(180deg, var(--red) 0%, var(--red-deep) 100%);
    display: flex; align-items: center; justify-content: center;
    font-family: "Poppins", sans-serif; font-weight: 700; font-size: 28px;
    color: var(--white); letter-spacing: .5px;
  }
  .store-band .divider { margin: 0 14px; }
</style>
</head>
<body>
  <main class="flyer">
    <div class="photo-toppings" role="img" aria-label="Pizza slices with basil and tomatoes seen from above"></div>
    <div class="photo-hero" role="img" aria-label="Close-up of a fresh pizza topped with ham, mushrooms, olives, corn and basil"></div>
    <div class="photo-table" role="img" aria-label="Rustic wooden table surface"></div>

    <div class="splash"></div>

    <div class="brand">
      <span class="brand-dot"></span>
      <span class="brand-name">Marlo's Pizzeria</span>
    </div>

    <h1 class="headline">
      <div class="headline-top">BUY ONE GET ONE</div>
      <div class="headline-free">FREE</div>
    </h1>

    <div class="hours-pill">OPEN AT 4PM DAILY!</div>

    <section class="terms">
      <p class="terms-line">(disclaimer: not valid for Mini Feast Tray or Crowd Pies)</p>
      <p class="terms-line">(we reserve the right to cancel this promotion at any time)</p>
      <p class="terms-note">This promotion has no limit and can be carryout or delivery. No coupon needed.</p>
    </section>

    <footer class="store-band">
      287 WEXFORD RD. E, Huron, OH<span class="divider">|</span>419-867-2093
    </footer>
  </main>
</body>
</html>
```